Modern and Clean Web Re-Design Project

We have 2 companies in similar industries: Printing and Mail Preparation/Fulfillment. We prefer sites that are clean and easy to navigate.Our printing company, Harbourline Press Works' website, hpwdirect.example is outdated needs revamping. We have rebranded our logo and are looking for a new design that is clean, modern and geared to other corporations and business in the downtown Toronto area. Our mailing company, The Postwick Depot (thepostwickdepot.example) needs a website as well. This company is in the Direct Mail and letter shop business, which essentially is addressing/personalizing people's printed matter and preparing it for either the Canadian or US postal service. The Postwick Depot specializes in not-for-profit and corporate sectors.Please see our logos to get an idea of the colors and look we want. For all intensive purposes, the sites can look similar in design all we want is that each site has the appropriate corporate colors and is a bit different so they don't look identical as the two business run as separate corporations.The content of the website should be easily changed by our staff and we want it to be setup to optimized for SEO based on the keywords we want. We are looking for someone to work on this project immediately
Updates

Project Deadline Extended
Reason: Change of ideas

After doing some thinking, I would like the site to be more modern but the non flash sites that I have seen so far Im finding life-less and while I want something clean, not overly busy and corporate looking, I dont want the design to be bland looking.

Please design with the previous specs in mind but with a twist as mentioned above.

Thanks
Dorian

Target Market(s)

See above

Industry/Entity Type

Printing

Requirements
Must have
• Must match the design and style of each respective logoSee the attached impage of the front of our offices to have an idea of our lookWe must be able to edit the content ourselves without any fancy programs or tools.Must be SEO optimized
Nice to have
• An online order form that can be emailed to us for quotes.....perhaps a page with a bunch of fields that have drop down menus....
Should not have
• Should not be overly busy. I want it to be clean and simple but informative without being hard to navigate

```html
<!DOCTYPE html>
<html lang="en">
<head>
<meta charset="utf-8">
<title>Harbourline Press Works</title>
<link href="https://fonts.googleapis.com/css2?family=Arimo:wght@400&display=swap" rel="stylesheet">
<style>
  :root {
    --brand-orange: #f0523a;
    --link-orange: #f26a3a;
    --text-dark: #111111;
    --white: #ffffff;
    --banner-start: #7f8a96;
    --banner-mid: #c9cfd6;
    --banner-end: #f2c21b;
    --photo-start: #d9dde2;
    --photo-mid: #9a9ea3;
    --photo-end: #e9b83a;
    --icon-blue: #3ab0e2;
    --icon-blue-light: #7fd3f3;
    --icon-amber: #f6922a;
    --icon-amber-light: #fbbd6d;
    --icon-navy: #3d64b0;
    --icon-navy-light: #7a9bd8;
    --reflect-blue: rgba(58, 176, 226, 0.35);
    --reflect-amber: rgba(246, 146, 42, 0.35);
    --reflect-navy: rgba(61, 100, 176, 0.35);
    --reflect-clear: rgba(240, 82, 58, 0);
  }
  * { margin: 0; padding: 0; box-sizing: border-box; }
  html, body { width: 1200px; height: 997px; overflow: hidden; background: var(--white); }
  body { position: relative; font-family: "Arimo", Arial, sans-serif; color: var(--text-dark); }

  .brand { position: absolute; left: 50px; top: 42px; display: flex; align-items: center; gap: 10px; }
  .brand-dot { width: 26px; height: 26px; border-radius: 50%; background: var(--brand-orange); }
  .brand-name { font-size: 20px; color: var(--brand-orange); }

  .contact { position: absolute; left: 945px; top: 15px; font-size: 18.5px; line-height: 23px; color: var(--link-orange); }

  .main-nav { position: absolute; right: 14px; top: 93px; display: flex; gap: 31px; font-size: 21.5px; color: var(--link-orange); white-space: nowrap; }

  .nav-band { position: absolute; left: 0; top: 124px; width: 1200px; height: 14px; background: var(--brand-orange); }

  .side-menu { position: absolute; left: 28px; top: 157px; width: 234px; height: 241px; border-radius: 8px; background: var(--brand-orange);
    color: var(--white); font-size: 21px; line-height: 26.7px; text-align: center; padding-top: 17px; }

  .hero-banner { position: absolute; left: 286px; top: 159px; width: 814px; height: 237px;
    background: linear-gradient(100deg, var(--banner-start) 0%, var(--banner-mid) 45%, var(--banner-end) 75%, #e8433a 100%); }

  .intro { position: absolute; left: 59px; top: 462px; width: 815px; font-size: 15.7px; line-height: 20px; }
  .intro p { text-indent: 28px; }
  .intro p.flush { text-indent: 0; }

  .team-photo { position: absolute; left: 889px; top: 461px; width: 213px; height: 320px;
    background: linear-gradient(180deg, var(--photo-start) 0%, var(--photo-mid) 55%, var(--photo-end) 85%, #555 100%); }

  .site-footer { position: absolute; left: 0; top: 873px; width: 1200px; height: 124px; background: var(--brand-orange); color: var(--white); }
  .solutions { position: absolute; top: 7px; font-size: 17.5px; line-height: 22.2px; }
  .solutions li { list-style: none; padding-left: 20px; }
  .solutions-a { left: 15px; }
  .solutions-b { left: 176px; }
  .solutions-c { left: 331px; }

  .social { position: absolute; left: 964px; top: 9px; display: flex; gap: 10px; }
  .social-item { display: flex; flex-direction: column; gap: 2px; }
  .social-tile { width: 57px; height: 57px; border-radius: 10px; box-shadow: inset 0 0 0 1px rgba(255,255,255,0.35); }
  .social-fade { width: 57px; height: 52px; border-radius: 10px 10px 0 0; }
  .tone-blue { background: linear-gradient(180deg, var(--icon-blue-light) 0%, var(--icon-blue) 55%); }
  .tone-amber { background: linear-gradient(180deg, var(--icon-amber-light) 0%, var(--icon-amber) 55%); }
  .tone-navy { background: linear-gradient(180deg, var(--icon-navy-light) 0%, var(--icon-navy) 55%); }
  .fade-blue { background: linear-gradient(180deg, var(--reflect-blue) 0%, var(--reflect-clear) 100%); }
  .fade-amber { background: linear-gradient(180deg, var(--reflect-amber) 0%, var(--reflect-clear) 100%); }
  .fade-navy { background: linear-gradient(180deg, var(--reflect-navy) 0%, var(--reflect-clear) 100%); }
</style>
</head>
<body>
  <header>
    <div class="brand"><span class="brand-dot"></span><span class="brand-name">Harbourline Press Works</span></div>
    <div class="contact">Phone 000-000-0000<br>your street, your town 00000</div>
    <nav class="main-nav">
      <span>Home</span><span>About Us</span><span>Our Products and Services</span><span>FAQ</span><span>Contact Us</span>
    </nav>
  </header>
  <div class="nav-band"></div>

  <nav class="side-menu">
    Why Us<br>Mailing Services<br>Printing Services<br>Mailing List<br>Management<br>Total Management<br>Services
  </nav>

  <div class="hero-banner" role="img" aria-label="Fanned spread of printed brochures and magazine covers"></div>

  <main class="intro">
    <p>Lorem ipsum dolor sit amet, consectetuer adipiscing elit. Aenean commodo ligula eget dolor. Aenean massa. Cum sociis natoque penatibus et magnis dis parturient montes, nascetur ridiculus mus. Donec quam felis, ultricies nec, pellentesque eu, pretium quis, sem.</p>
    <p>Nulla consequat massa quis enim. Donec pede justo, fringilla vel, aliquet nec, vulputate eget, arcu. In enim justo, rhoncus ut, imperdiet a, venenatis vitae, justo. Nullam dictum felis eu pede mollis pretium. Integer tincidunt. Cras dapibus. Vivamus elementum semper nisi. Aenean vulputate eleifend tellus. Aenean leo ligula, porttitor eu, consequat vitae, eleifend ac, enim. Aliquam lorem ante, dapibus in, viverra quis, feugiat a, tellus. Phasellus viverra nulla ut metus varius laoreet. Quisque rutrum. Aenean imperdiet. Etiam ultricies nisi vel augue. Curabitur ullamcorper ultricies nisi. Nam eget dui.</p>
    <p class="flush">Etiam rhoncus. Maecenas tempus, tellus eget condimentum rhoncus, sem quam semper libero, sit amet adipiscing sem neque sed ipsum.</p>
    <p>Nam quam nunc, blandit vel, luctus pulvinar, hendrerit id, lorem. Maecenas nec odio et ante tincidunt tempus. Donec vitae sapien ut libero venenatis faucibus. Nullam quis ante. Etiam sit amet orci eget eros faucibus tincidunt. Duis leo. Sed fringilla mauris sit amet nibh. Donec sodales sagittis magna. Sed consequat, leo eget bibendum sodales, augue velit cursus nunc,</p>
  </main>

  <div class="team-photo" role="img" aria-label="Staff member standing beside a mail processing machine in the production shop"></div>

  <footer class="site-footer">
    <ul class="solutions solutions-a">Solutions for:<li>Healthcare</li><li>Small Business</li><li>High Tech</li><li>More...</li></ul>
    <ul class="solutions solutions-b">Solutions for:<li>Healthcare</li><li>Small Business</li><li>High Tech</li><li>More...</li></ul>
    <ul class="solutions solutions-c">Solutions for:<li>Healthcare</li><li>Small Business</li><li>High Tech</li><li>More...</li></ul>
    <div class="social">
      <div class="social-item"><span class="social-tile tone-blue"></span><span class="social-fade fade-blue"></span></div>
      <div class="social-item"><span class="social-tile tone-amber"></span><span class="social-fade fade-amber"></span></div>
      <div class="social-item"><span class="social-tile tone-navy"></span><span class="social-fade fade-navy"></span></div>
    </div>
  </footer>
</body>
</html>
```